Specialised investor in e-mobility and energy wants business card design

We need a business card design that fits our existing corporate design. <The look and feel must be 'sharp'/'clean', dynamic, communicate momentum, professionalism etc (as one would imagine from a firm in the financial sector). We like the idea of a reverse-side of the card that includes the logo, and the name and contact details on the other. We expect the deliverable to be whatever format might be required to be able to get cards printed directly by a service such as tandor press. Our website is www.orm.capital

```html
<!DOCTYPE html>
<html lang="en">
<head>
<meta charset="utf-8">
<title>ORM Capital – Business Card</title>
<link href="https://fonts.googleapis.com/css2?family=Roboto:wght@400;700&display=swap" rel="stylesheet">
<style>
  :root {
    --backdrop: #989898;
    --forest: #314f23;
    --forest-ink: #2c4620;
    --forest-mark: #3f5f30;
    --leaf: #8ab04a;
    --paper: #ffffff;
    --text-grey: #7a7a7a;
    --rule: #c9c9c9;
  }
  * { margin: 0; padding: 0; box-sizing: border-box; }
  html, body {
    width: 1200px;
    height: 1000px;
    overflow: hidden;
    background: var(--backdrop);
    font-family: "Roboto", Arial, sans-serif;
  }
  .card {
    position: absolute;
    left: 293px;
    width: 615px;
    height: 351px;
  }
  .card--front {
    top: 100px;
    background: var(--forest);
    display: flex;
    align-items: center;
    justify-content: center;
  }
  .front-wordmark {
    color: var(--forest-mark);
    font-weight: 400;
    font-size: 56px;
    letter-spacing: 1px;
  }
  .card--back {
    top: 511px;
    background: var(--paper);
  }
  .back-wordmark {
    position: absolute;
    left: 40px;
    width: 240px;
    top: 118px;
    text-align: center;
    color: var(--forest-ink);
    font-weight: 400;
    font-size: 46px;
    line-height: 1.1;
  }
  .divider {
    position: absolute;
    left: 307px;
    top: 87px;
    width: 1px;
    height: 176px;
    background: var(--rule);
  }
  .details {
    position: absolute;
    left: 350px;
    top: 100px;
  }
  .person-name {
    color: var(--forest-ink);
    font-weight: 700;
    font-size: 22px;
    line-height: 26px;
  }
  .person-role {
    color: var(--leaf);
    font-weight: 400;
    font-size: 22px;
    line-height: 30px;
  }
  .contact-list {
    list-style: none;
    margin-top: 14px;
  }
  .contact-item {
    display: flex;
    align-items: center;
    height: 26px;
    color: var(--text-grey);
    font-size: 18px;
  }
  .contact-icon {
    width: 18px;
    height: 18px;
    margin-right: 10px;
    fill: var(--leaf);
    flex: none;
  }
</style>
</head>
<body>

<section class="card card--front" aria-label="Card front">
  <span class="front-wordmark">ORM Capital</span>
</section>

<section class="card card--back" aria-label="Card back">
  <div class="back-wordmark">ORM<br>Capital</div>
  <div class="divider"></div>
  <div class="details">
    <p class="person-name">Martin Ellery</p>
    <p class="person-role">Partner</p>
    <ul class="contact-list">
      <li class="contact-item">
        <svg class="contact-icon" viewBox="0 0 18 18" aria-hidden="true">
          <path d="M5 0h8a1 1 0 0 1 1 1v16a1 1 0 0 1-1 1H5a1 1 0 0 1-1-1V1a1 1 0 0 1 1-1zm1 2v11h6V2zm3 12.5a1 1 0 1 0 0 2 1 1 0 0 0 0-2z"/>
        </svg>
        +41 79555 0148
      </li>
      <li class="contact-item">
        <svg class="contact-icon" viewBox="0 0 18 18" aria-hidden="true">
          <path d="M0 4h18v11H0zm1.5 1.3v.4L9 10.5l7.5-4.8v-.4zm0 2.1v6.3l4.5-3.4zm15 0L12 10.3l4.5 3.4z"/>
        </svg>
        martin@orm.capital
      </li>
      <li class="contact-item">
        <svg class="contact-icon" viewBox="0 0 18 18" aria-hidden="true">
          <path d="M9 1.5a7.5 7.5 0 1 0 0 15 7.5 7.5 0 0 0 0-15zm-5.9 6.7h2.5c.1-1.7.5-3.2 1.1-4.3A6 6 0 0 0 3.1 8.2zm0 1.6a6 6 0 0 0 3.6 4.3c-.6-1.1-1-2.6-1.1-4.3zm4.1 0c.1 2.4.9 4.3 1.8 4.8.9-.5 1.7-2.4 1.8-4.8zm3.6-1.6c-.1-2.4-.9-4.3-1.8-4.8-.9.5-1.7 2.4-1.8 4.8zm1.6 1.6c-.1 1.7-.5 3.2-1.1 4.3a6 6 0 0 0 3.6-4.3zm2.5-1.6a6 6 0 0 0-3.6-4.3c.6 1.1 1 2.6 1.1 4.3z"/>
        </svg>
        www.orm.capital
      </li>
    </ul>
  </div>
</section>

</body>
</html>
```